A4 Flyer Design outlining our financial philosophy

One A4 page design (landscape orientation) outlining our financial philosophy.
The design needs to show these steps as the building blocks and the path taken to financial success:
1. Maximise income and reduce expenses
2. Maximise savings and reduce bad debts
3. Invest wisely & tax effectively
4. Manage risk
5. Plan for retirement
6. Leave a legacy
The design needs to incorporate the 6 building blocks above along with the key points for each topic. More info attached.
Design must be engaging, professional and consistent with our current branding colours.

Target Market(s)

self employed individuals looking to build wealth through property and shares.

Industry/Entity Type

Financial Planning

Font styles to use
Sans Serif

Colors
0255a3
5c5c5c
000000
ffffff

Requirements
Must have
• clear and engaging.
• consistent with current branding
• 6 topics with key considerations (as per attached)
• must show that all 6 points are linked and are a journey.

```html
<!DOCTYPE html>
<html lang="en">
<head>
<meta charset="utf-8">
<title>Our Financial Philosophy – Meridian Financial Group</title>
<link rel="stylesheet" href="https://fonts.googleapis.com/css2?family=Oswald:wght@500;600&family=Open+Sans:wght@400;600&family=Arvo:wght@400;700&display=swap">
<style>
  :root {
    --brand: #0255a3;
    --brand-bright: #2452e6;
    --bg-light: #1c7af0;
    --bg-deep: #0b3fd6;
    --heading: #2150e0;
    --text: #3a3a3a;
    --muted: #5c5c5c;
    --rule: #d9dde6;
    --white: #ffffff;
    --navy: #17349a;
  }
  * { box-sizing: border-box; margin: 0; padding: 0; }
  html, body { width: 1200px; height: 848px; overflow: hidden; }
  body { font-family: "Open Sans", Arial, sans-serif; background: var(--bg-deep); }

  .flyer { position: relative; width: 1200px; height: 848px; overflow: hidden; }

  .backdrop {
    position: absolute; inset: 0;
    background:
      radial-gradient(ellipse 60% 55% at 50% 35%, rgba(120,190,255,0.45), transparent 70%),
      linear-gradient(180deg, var(--bg-light) 0%, #1466ea 45%, var(--bg-deep) 100%);
  }

  .brand-box {
    position: absolute; left: 467px; top: 24px; width: 265px; height: 83px;
    background: var(--white);
    display: flex; align-items: center; justify-content: center; gap: 12px;
  }
  .brand-dot { width: 58px; height: 58px; border-radius: 50%; background: var(--navy); flex: none; }
  .brand-name {
    font-family: "Oswald", sans-serif; font-weight: 600; color: var(--navy);
    font-size: 21px; line-height: 1.05; letter-spacing: 1px; text-transform: uppercase;
  }

  .title-row { position: absolute; left: 0; top: 120px; width: 1200px; height: 42px; }
  .title-line { position: absolute; top: 19px; height: 3px; background: var(--white); }
  .title-line.left { left: 173px; width: 136px; }
  .title-line.right { left: 892px; width: 135px; }
  .title-gem { position: absolute; top: 14px; width: 11px; height: 11px; background: var(--white); transform: rotate(45deg); }
  .title-gem.left { left: 334px; }
  .title-gem.right { left: 855px; }
  .page-title {
    position: absolute; left: 0; width: 1200px; top: 0; text-align: center;
    font-family: "Arvo", serif; font-weight: 400; font-size: 32px; line-height: 42px;
    color: var(--white); letter-spacing: 0.5px;
  }

  .path-line { position: absolute; left: 599px; top: 255px; width: 2px; height: 422px; background: rgba(255,255,255,0.55); }
  .path-plus {
    position: absolute; width: 25px; height: 25px; border-radius: 50%;
    background: var(--brand-bright); border: 2px solid rgba(255,255,255,0.6);
    color: var(--white); font: 700 20px/20px "Open Sans", sans-serif; text-align: center;
    left: 588px;
  }
  .path-chevrons { position: absolute; left: 591px; width: 18px; }

  .step {
    position: absolute; width: 352px; height: 155px; background: var(--white);
    padding: 16px 22px 0 23px;
    box-shadow: 0 2px 6px rgba(0,20,90,0.25);
  }
  .step.col-left { left: 172px; }
  .step.col-right { left: 674px; padding-left: 28px; }
  .step.row-1 { top: 177px; }
  .step.row-2 { top: 365px; }
  .step.row-3 { top: 553px; }

  .step-title {
    font-family: "Oswald", sans-serif; font-weight: 500; font-size: 22px; line-height: 28px;
    color: var(--heading); padding-bottom: 5px; border-bottom: 1px solid var(--rule); white-space: nowrap;
  }
  .step-title small { font-size: 13px; }
  .key-points { list-style: none; margin-top: 10px; }
  .key-points li {
    position: relative; padding-left: 21px; margin-bottom: 7px;
    font-size: 10px; line-height: 11.5px; color: var(--text);
  }
  .key-points li::before {
    content: ""; position: absolute; left: 0; top: 1px; width: 9px; height: 9px;
    background: var(--brand-bright); border-radius: 1.5px;
  }
  .key-points li::after {
    content: ""; position: absolute; left: 2.5px; top: 2.5px; width: 3px; height: 5px;
    border: solid var(--white); border-width: 0 1.5px 1.5px 0; transform: rotate(40deg);
  }
  .key-points.roomy li { margin-bottom: 10px; }

  .step-number {
    position: absolute; width: 31px; height: 31px; background: var(--brand-bright);
    transform: rotate(45deg); top: 62px;
  }
  .col-left .step-number { right: -16px; }
  .col-right .step-number { left: -16px; }
  .step-number span {
    position: absolute; inset: 0; transform: rotate(-45deg);
    font-family: "Oswald", sans-serif; font-weight: 500; font-size: 20px; line-height: 31px;
    color: var(--white); text-align: center;
  }

  .result-gem {
    position: absolute; left: 575px; top: 694px; width: 50px; height: 50px;
    background: var(--white); transform: rotate(45deg);
  }
  .result-label {
    position: absolute; left: 560px; top: 706px; width: 80px; text-align: center;
    font-family: "Arvo", serif; font-weight: 700; font-size: 11.5px; line-height: 11px; color: var(--brand-bright);
  }
  .result-headline {
    position: absolute; left: 0; width: 1200px; top: 768px; text-align: center;
    font-family: "Oswald", sans-serif; font-weight: 500; font-size: 35px; line-height: 48px; color: var(--white);
  }
</style>
</head>
<body>
<main class="flyer">
  <div class="backdrop" role="img" aria-label="Blue abstract backdrop with faint finance arrows, dot grid and a celebrating businessman silhouette"></div>

  <header class="brand-box">
    <span class="brand-dot"></span>
    <span class="brand-name">Meridian<br>Financial Group</span>
  </header>

  <div class="title-row">
    <span class="title-line left"></span><span class="title-gem left"></span>
    <h1 class="page-title">OUR FINANCIAL PHILOSOPHY</h1>
    <span class="title-gem right"></span><span class="title-line right"></span>
  </div>

  <div class="path-line"></div>
  <div class="path-plus" style="top:243px">+</div>
  <div class="path-plus" style="top:431px">+</div>
  <div class="path-plus" style="top:622px">+</div>
  <svg class="path-chevrons" style="top:332px" width="18" height="28" viewBox="0 0 18 28" aria-hidden="true">
    <g fill="none" stroke="#2e5fe8" stroke-width="2.5"><path d="M3 2l6 6 6-6"/><path d="M3 10l6 6 6-6"/><path d="M3 18l6 6 6-6"/></g>
  </svg>
  <svg class="path-chevrons" style="top:523px" width="18" height="28" viewBox="0 0 18 28" aria-hidden="true">
    <g fill="none" stroke="#2e5fe8" stroke-width="2.5"><path d="M3 2l6 6 6-6"/><path d="M3 10l6 6 6-6"/><path d="M3 18l6 6 6-6"/></g>
  </svg>

  <section class="step col-left row-1">
    <h2 class="step-title">Maximise Income &amp; Reduce Expenses</h2>
    <ul class="key-points">
      <li>Invest in yourself through education and training</li>
      <li>Align your spending with your values</li>
      <li>Build a number of income streams</li>
      <li>Increase surplus income</li>
      <li>Track your spending</li>
    </ul>
    <div class="step-number"><span>1</span></div>
  </section>

  <section class="step col-right row-1">
    <h2 class="step-title">Maximise Savings <small>/ Wquity &amp; Reduce Bad Debts</small></h2>
    <ul class="key-points roomy">
      <li>Surplus income in creases savings</li>
      <li>Use savings and equity for investment</li>
      <li>Avoid borrowing for lifestyle assets / experiences where possible</li>
    </ul>
    <div class="step-number"><span>2</span></div>
  </section>

  <section class="step col-left row-2">
    <h2 class="step-title">Invest Wisely &amp; Effectively</h2>
    <ul class="key-points">
      <li>Build an investment portfolio e.g. property and shares</li>
      <li>Use appropriate tax structures such as Family Trusts / Superannuation</li>
      <li>Depreciation schedules</li>
    </ul>
    <div class="step-number"><span>3</span></div>
  </section>

  <section class="step col-right row-2">
    <h2 class="step-title">Manage Risk</h2>
    <ul class="key-points roomy">
      <li>Insurance in various forms</li>
      <li>Contingency plans</li>
      <li>Diversification</li>
      <li>Focus on quality</li>
    </ul>
    <div class="step-number"><span>4</span></div>
  </section>

  <section class="step col-left row-3">
    <h2 class="step-title">Plan For Retirement</h2>
    <ul class="key-points">
      <li>Replacement of your salary or profits from running a business with income from your investment portfolio nest egg</li>
      <li>Drawing a sustainable income to maintain a great lifestyle and protect your retirement nest egg</li>
    </ul>
    <div class="step-number"><span>5</span></div>
  </section>

  <section class="step col-right row-3">
    <h2 class="step-title">Leave Legacy</h2>
    <ul class="key-points">
      <li>Having a Will</li>
      <li>Power of Attorney</li>
      <li>Testamentary Trust?</li>
    </ul>
    <div class="step-number"><span>6</span></div>
  </section>

  <div class="result-gem"></div>
  <div class="result-label">The<br>Result</div>
  <p class="result-headline">Financial Success</p>
</main>
</body>
</html>
```